Morrow Engineering Core Values Branding Package

Morrow Engineering has recently refined its company Core Values and is seeking a strong, cohesive branding package to visually bring these values to life. The new graphic assets will communicate our commitment to excellence in a way that resonates with our team, clients, and partners in a blue-collar, industrial environment.

We are looking for multiple visual assets with consistent design elements that can be applied across platforms. The tone should reflect strength, reliability, and professionalism while remaining approachable and aligned with our industry.

Core Values & Descriptions
Accountability
“We take ownership of our work and actions, ensuring reliability and trust in every solution we deliver.”

Teamwork
“We collaborate across departments and disciplines to provide the highest level of service and innovation for our clients.”

Integrity
“We operate with honesty, transparency, and ethical standards in all aspects of our business.”

Growth
“We are committed to continuous improvement—of our people, our processes, and our impact in the industry.”

Deliverables

1. Primary Core Values Graphic
A master visual representing all four values together.
Designed for use on posters, office signage, internal presentations.

2. Individual Value Graphics (x4)
One graphic per core value: Accountability, Teamwork, Integrity, Growth.
Cohesive style with slight visual variation to reflect each value’s unique meaning.

Target Market(s)

Employees of Morrow Engineering

Industry/Entity Type

Blue Collar

Font styles to use
Sans Serif

Colors
0054AA
0677BA
7BADD7
CADEEF
E8F1F8
00AB8E
00BBA5
67D7C9
C6EFE9
E9F9F6
EB3D1F
EC4F4E
F09395
F8D3D4
FCEDEE

Requirements
Must have
• Accountability, Teamwork, Integrity, Growth

```html
<!DOCTYPE html>
<html lang="en">
<head>
<meta charset="utf-8">
<title>Morrow Engineering – Core Values</title>
<link href="https://fonts.googleapis.com/css2?family=Anton&family=Arimo:wght@400;700&display=swap" rel="stylesheet">
<style>
  :root {
    --backdrop: #555555;
    --navy: #003163;
    --side-band: #1d4878;
    --band-text: #8fa3bf;
    --green: #3aaa35;
    --white: #ffffff;
    --url-grey: #6f87a8;
    --icon-tone: #2b2b2b;
  }
  * { margin: 0; padding: 0; box-sizing: border-box; }
  html, body {
    width: 731px; height: 1200px; overflow: hidden;
    background: var(--backdrop);
  }
  .poster {
    position: absolute; left: 9px; top: 100px;
    width: 712px; height: 1000px;
    background: var(--navy);
    font-family: "Arimo", Arial, sans-serif;
    box-shadow: 0 4px 14px rgba(0,0,0,.45);
    overflow: hidden;
  }
  .side-band {
    position: absolute; left: 0; top: 0; width: 140px; height: 100%;
    background: var(--side-band);
    overflow: hidden;
  }
  .side-title {
    position: absolute; left: 16px; top: 968px;
    transform: rotate(-90deg); transform-origin: 0 0;
    font-family: "Arimo", Arial, sans-serif; font-weight: 700;
    font-size: 122px; line-height: 1; color: var(--band-text);
    white-space: nowrap;
  }
  .brand-name {
    position: absolute; left: 186px; top: 104px;
    font-family: "Arimo", Arial, sans-serif; font-weight: 700;
    font-size: 60px; line-height: 1; color: var(--white);
  }
  .value-icon {
    position: absolute; left: 164px; width: 110px; height: 110px;
    border-radius: 50%; background: var(--white);
    border: 6px solid var(--green);
    display: flex; align-items: center; justify-content: center;
  }
  .value-icon .pictogram {
    width: 56px; height: 56px; border-radius: 50%;
    background: radial-gradient(circle, #444 0%, var(--icon-tone) 70%);
  }
  .value-title {
    position: absolute; left: 293px;
    font-family: "Anton", Impact, sans-serif; font-weight: 400; font-size: 40px;
    line-height: 1; color: var(--green); letter-spacing: -0.5px;
  }
  .value-text {
    position: absolute; left: 293px; width: 340px;
    font-size: 15px; font-weight: 700; line-height: 20px; color: var(--white);
  }
  .divider {
    position: absolute; left: 196px; width: 466px; height: 2px;
    background: var(--green);
  }
  .divider::before {
    content: ""; position: absolute; left: -1px; top: -4px;
    width: 10px; height: 10px; border-radius: 50%; background: var(--green);
  }
  .site-url {
    position: absolute; right: 52px; top: 946px;
    font-size: 19px; font-weight: 700; letter-spacing: 2.5px; color: var(--url-grey);
  }
</style>
</head>
<body>
  <main class="poster">
    <div class="side-band">
      <h1 class="side-title">CORE VALUES</h1>
    </div>

    <div class="brand-name">MORROW</div>

    <div class="value-icon" style="top:262px;"><div class="pictogram" role="img" aria-label="Accountability pictogram: document, magnifier and person"></div></div>
    <h2 class="value-title" style="top:262px;">ACCOUNTABILITY:</h2>
    <p class="value-text" style="top:306px;">We take ownership of our work and actions, ensuring reliability and trust in every solution we deliver.</p>
    <div class="divider" style="top:395px;"></div>

    <div class="value-icon" style="top:420px;"><div class="pictogram" role="img" aria-label="Teamwork pictogram: clasped hands"></div></div>
    <h2 class="value-title" style="top:422px;">TEAMWORK:</h2>
    <p class="value-text" style="top:466px;">We collaborate across departments and disciplines to provide the highest level of service and innovation for our clients.</p>
    <div class="divider" style="top:559px;"></div>

    <div class="value-icon" style="top:585px;"><div class="pictogram" role="img" aria-label="Integrity pictogram: gear with people and arrows"></div></div>
    <h2 class="value-title" style="top:592px;">INTEGRITY:</h2>
    <p class="value-text" style="top:636px;">We operate with honesty, transparency, and ethical standards in all aspects of our business.</p>
    <div class="divider" style="top:727px;"></div>

    <div class="value-icon" style="top:758px;"><div class="pictogram" role="img" aria-label="Growth pictogram: rising bars with arrow"></div></div>
    <h2 class="value-title" style="top:757px;">GROWTH:</h2>
    <p class="value-text" style="top:801px;">We are committed to continuous improvement—of our people, our processes, and our impact in the industry.</p>

    <div class="site-url">WWW.MORROWENG.COM</div>
  </main>
</body>
</html>
```